Real Estate Website - Phase I

We are looking to re-design our company website completely.
This will be for a real estate company which focuses on multiple lines of business/customers, including

1) Buyers - Investors, Owner Occupants
2) Sellers - Short Sales, Limited Services/Flat Fee, and Corporate/REO clients (the last being our core current customer)
3) Other Services: Default Services, Institutional Property Management, Field and Inspection Services
4) Agent FAQ's, instructions, etc to tie into our web-based offer management systems

For a brief understanding of what we do - Please see www.plavetrix.com. Current site does not address all of our current services.

Website must be able to be edited/added onto over time. We are also looking at redirects so that certain pages/sections can be given unique domain names to drive core customers to.

We work both with normal agents and buyers and large scale financial institutions, therefore our focus must be specific to each unique group based on the applicable page(s).

We had an incorrect amount in this brief.  It has since been corrected.

Please re-review.

Industry/Entity Type

Real Estate

Requirements
Must have
• *Property Search/Display - By various criteria AND by map
*Property Management back end for putting in new properties
*MObile Version or Mobile Friendly
*Analytics
*Contact Management and Lead Capture functions, including ability to export or use from site for email marketing campaigns. Lead capture must be able to sort by various criteria to tailor campaigns, ability to send out auto notices to staff and those signing up, etc.
* Signup option w/ functions for viewing not yet on market properties (subscription). This needs to be able to let buyers set search criteria and be auto notified whenever a property was listed or adjusted that met their criteria.
* SEO Optimization
* Syndication options to allow ease of syndication
* FAQ's and assistance pages to agents working with us
* Blog, social media boxes
* Ability for buyers to submit initial offers direct
* Functions and pages specific to below, with ability to cross promote and track (inquiry forms, etc to the below)
*Dedicated or preferred lender(s)
* Preferred vendors, etc

```html
<!DOCTYPE html>
<html lang="en">
<head>
<meta charset="utf-8">
<title>Plavetrix Realty</title>
<link href="https://fonts.googleapis.com/css2?family=PT+Sans:wght@400;700&family=PT+Sans+Narrow:wght@400;700&display=swap" rel="stylesheet">
<style>
:root{
  --navy:#2a3592;
  --navy-dark:#222a78;
  --nav-top:#4d5cc6;
  --nav-bottom:#2d3996;
  --ink:#1d2240;
  --muted:#6b6f86;
  --yellow:#f3b816;
  --yellow-dark:#e2a006;
  --brown:#5a3a06;
  --line:#e1e4ef;
  --panel:#f7f9fd;
}
*{box-sizing:border-box;margin:0;padding:0}
html,body{width:821px;height:1200px;overflow:hidden;background:#fff}
body{font-family:"PT Sans",Arial,sans-serif;color:var(--ink);position:relative}
.page{position:relative;width:821px;height:1200px;background:linear-gradient(#f2f5fc 0,#e7ecf8 130px,#fff 131px)}
.abs{position:absolute}
.top-rule{left:0;top:0;width:821px;height:3px;background:#d9deec}

.brand{left:53px;top:25px;display:flex;align-items:center;gap:6px}
.brand-mark{width:48px;height:54px;background:var(--navy)}
.brand-name{font-size:22px;font-weight:700;color:var(--navy);line-height:1;letter-spacing:.5px}
.contact{left:582px;top:32px;font-size:11px;line-height:17px;color:var(--navy)}
.contact b{font-weight:700}

.nav{left:50px;top:93px;width:721px;height:38px;background:linear-gradient(var(--nav-top),var(--nav-bottom));display:flex;border-radius:2px 2px 0 0}
.nav a{color:#fff;text-decoration:none;font-size:12.5px;display:flex;align-items:center;padding:0 15px;border-right:1px solid #24307f;box-shadow:1px 0 0 #5f6ed0}
.nav .home{width:46px;justify-content:center;padding:0}

.hero{left:50px;top:138px;width:502px;height:263px;background:var(--panel);border:1px solid var(--line)}
.hero-photo{position:absolute;left:0;top:0;width:502px;height:207px;background:linear-gradient(#c9d8e4,#bfc6b7 40%,#6f8a48 75%,#4f6a2e)}
.dots{position:absolute;left:228px;top:193px;display:flex;gap:3px}
.dots i{width:7px;height:7px;border-radius:50%;background:#fff;display:block}
.thumbs{position:absolute;left:18px;top:216px;display:flex;gap:10px}
.thumbs span{width:45px;height:38px;border:3px solid #fff;box-shadow:0 0 2px #aab;display:block}

.search{left:559px;top:138px;width:212px;height:263px;background:var(--yellow-dark);border:1px solid #d69a05;border-radius:2px}
.search h2{height:39px;background:var(--yellow);font-size:15.5px;color:var(--brown);padding:12px 0 0 20px;font-weight:700}
.field{position:absolute;left:16px;width:176px;height:22px;background:#fff;border-radius:2px;font-size:9.5px;color:#8a8a8a;padding:5px 10px}
.field.half{width:84px}
.btn-search{position:absolute;left:16px;top:207px;width:76px;height:23px;background:var(--brown);color:#fff;font-size:10px;font-weight:700;border-radius:2px;display:flex;align-items:center;justify-content:center}

.card{top:417px;width:231px;height:123px;background:var(--panel);border:1px solid var(--line);padding:14px 20px;box-shadow:0 2px 3px rgba(0,0,0,.05)}
.card h3{font-size:14px;color:var(--navy-dark);font-weight:700;margin-bottom:3px}
.card p{font-size:8.5px;line-height:14px;color:var(--muted)}
.btn{display:inline-flex;margin-top:7px;width:80px;height:23px;background:var(--yellow);border:1px solid var(--yellow-dark);border-radius:3px;color:#fff;font-family:"PT Sans Narrow",sans-serif;font-size:10.5px;font-weight:700;align-items:center;justify-content:center}

.latest{left:53px;top:573px;width:484px;height:538px;border:1px solid var(--line);border-radius:2px;background:linear-gradient(#f6f8fd,#fff 200px)}
.latest h2{position:absolute;left:20px;top:18px;font-size:15px;font-weight:700;color:var(--ink)}
.more{position:absolute;left:366px;top:25px;font-size:8.5px;color:var(--navy)}
.listing{position:absolute;left:18px;width:450px;height:96px}
.listing .photo{position:absolute;left:0;top:0;width:151px;height:96px;border:4px solid #eceef3;background:linear-gradient(#a9c3e2,#d8d2c0 55%,#5f8a3a)}
.listing .info{position:absolute;left:163px;top:0;width:285px}
.listing h4{font-size:10px;font-weight:700;margin-bottom:6px}
.meta{display:grid;grid-template-columns:95px 1fr;font-size:8.5px;line-height:17px;color:#333}
.listing p{font-size:8.5px;line-height:14px;color:#444;margin-top:6px}

.news{left:552px;top:573px;width:214px;height:310px;border:1px solid var(--line);background:#fff}
.news h2,.top h2{height:35px;font-size:14.5px;font-weight:700;color:#fff;padding:10px 0 0 20px}
.news h2{background:linear-gradient(var(--nav-top),var(--nav-bottom))}
.entry{margin:0 18px 0 20px;padding:12px 0 8px;border-bottom:1px solid #ccd}
.entry:last-child{border-bottom:0}
.entry time{display:block;font-size:9px;color:#333;margin-bottom:4px}
.entry p{font-size:8.5px;line-height:14px;color:var(--muted)}

.top{left:550px;top:892px;width:213px;height:208px;border:1px solid var(--line);background:#fff}
.top h2{background:var(--yellow-dark)}
.top ul{list-style:none;padding:10px 40px 0 24px}
.top li{font-size:8.5px;height:24px;line-height:23px;border-bottom:1px solid #e9eaf0;position:relative;padding-left:13px;color:var(--ink)}
.top li:last-child{border-bottom:0}
.top li::before{content:"›";position:absolute;left:0;color:#999;font-size:11px}

.footer{left:0;top:1130px;width:821px;height:70px;background:linear-gradient(#3643a8,#4350b6 60%,#3945a6);border-top:3px solid #232c85}
.copy{position:absolute;left:62px;top:26px;font-size:8.5px;color:#aeb5e6}
.flinks{position:absolute;left:390px;top:28px;font-size:8.5px;color:#fff}
.flinks span{color:#aeb5e6;margin:0 4px}
.social{position:absolute;left:718px;top:22px;display:flex;gap:6px}
.social i{width:15px;height:15px;border-radius:50%;background:#fff;display:block}
</style>
</head>
<body>
<div class="page">
  <div class="abs top-rule"></div>

  <div class="abs brand">
    <span class="brand-mark"></span>
    <span class="brand-name">PLAVETRIX REALTY</span>
  </div>

  <div class="abs contact">
    <b>Plavetrix Realty</b><br>
    Main: 555-014-0032 &nbsp;/&nbsp; Fax: 555-014-4589<br>
    Email add: &nbsp;info@plavetrix.com
  </div>

  <nav class="abs nav">
    <a class="home" href="#" aria-label="Home">
      <svg width="16" height="15" viewBox="0 0 16 15"><path d="M8 0 0 7h2v8h4v-5h4v5h4V7h2z" fill="#fff"/></svg>
    </a>
    <a href="#">Our Listings</a>
    <a href="#">Buyers</a>
    <a href="#">Short Sales</a>
    <a href="#">Agents</a>
    <a href="#">Asset Managers</a>
    <a href="#">Contact Us</a>
  </nav>

  <section class="abs hero">
    <div class="hero-photo" role="img" aria-label="Photo of a white porch house with garden and iron fence"></div>
    <div class="dots"><i></i><i></i><i></i><i></i><i></i></div>
    <div class="thumbs">
      <span role="img" aria-label="House thumbnail" style="background:linear-gradient(#9fc0e0,#7a9a5a)"></span>
      <span role="img" aria-label="House thumbnail" style="background:linear-gradient(#dfe6ec,#a7b39a)"></span>
      <span role="img" aria-label="House thumbnail" style="background:linear-gradient(#6f98d0,#6e8d58)"></span>
      <span role="img" aria-label="Interior thumbnail" style="background:linear-gradient(#e9dccd,#b98f6a)"></span>
      <span role="img" aria-label="Pool at dusk thumbnail" style="background:linear-gradient(#24407a,#3a82b0)"></span>
    </div>
  </section>

  <aside class="abs search">
    <h2>Search Property</h2>
    <div class="field" style="top:51px">Keyword</div>
    <div class="field" style="top:81px">All Types</div>
    <div class="field" style="top:112px">State / Countries</div>
    <div class="field half" style="top:143px">Price Range</div>
    <div class="field half" style="top:143px;left:108px">Price Range</div>
    <div class="field" style="top:175px">Locations</div>
    <div class="btn-search">Search Now</div>
  </aside>

  <div class="abs card" style="left:50px">
    <h3>BUYERS</h3>
    <p>Mauris vel lacus vitae felis vestibulum volutpat. Etiam est nunc, venenatis in, tristique eu, imperdiet ac, nisl. Cum sociis natoque penatibus et</p>
    <span class="btn">CLICK HERE</span>
  </div>
  <div class="abs card" style="left:295px">
    <h3>AGENTS</h3>
    <p>Mauris vel lacus vitae felis vestibulum volutpat. Etiam est nunc, venenatis in, tristique eu, imperdiet ac, nisl. Cum sociis natoque penatibus et</p>
    <span class="btn">CLICK HERE</span>
  </div>
  <div class="abs card" style="left:539px">
    <h3>ASSET MANAGERS</h3>
    <p>Mauris vel lacus vitae felis vestibulum volutpat. Etiam est nunc, venenatis in, tristique eu, imperdiet ac, nisl. Cum sociis natoque penatibus et</p>
    <span class="btn">CLICK HERE</span>
  </div>

  <section class="abs latest">
    <h2>Latest Properties</h2>
    <span class="more">View More Properties</span>

    <article class="listing" style="top:56px">
      <div class="photo" role="img" aria-label="Photo of a yellow two-storey house"></div>
      <div class="info">
        <h4>Tala 2 bedroom Apartments</h4>
        <div class="meta"><span>Area : 117 (Sq.M.)</span><span>Property ID : 14353</span><span>Bedrooms : 3</span><span>Posted on : March 2, 2013</span></div>
        <p>Mauris vel lacus vitae felis vestibulum volutpat. Etiam est nunc, venenatis in, tristique eu, imperdiet ac, nisl. Cum sociis natoque penatibus et magnis dis parturient montes,</p>
      </div>
    </article>
    <article class="listing" style="top:180px">
      <div class="photo" role="img" aria-label="Photo of a white house with a large tree" style="background:linear-gradient(#d6dde4,#c9c4b6 55%,#5c8236)"></div>
      <div class="info">
        <h4>Tala 2 bedroom Apartments</h4>
        <div class="meta"><span>Area : 117 (Sq.M.)</span><span>Property ID : 14353</span><span>Bedrooms : 3</span><span>Posted on : March 2, 2013</span></div>
        <p>Mauris vel lacus vitae felis vestibulum volutpat. Etiam est nunc, venenatis in, tristique eu, imperdiet ac, nisl. Cum sociis natoque penatibus et magnis dis parturient montes,</p>
      </div>
    </article>
    <article class="listing" style="top:302px">
      <div class="photo" role="img" aria-label="Photo of a brick house with garage" style="background:linear-gradient(#4f86cf,#a58070 55%,#5f8d3a)"></div>
      <div class="info">
        <h4>Tala 2 bedroom Apartments</h4>
        <div class="meta"><span>Area : 117 (Sq.M.)</span><span>Property ID : 14353</span><span>Bedrooms : 3</span><span>Posted on : March 2, 2013</span></div>
        <p>Mauris vel lacus vitae felis vestibulum volutpat. Etiam est nunc, venenatis in, tristique eu, imperdiet ac, nisl. Cum sociis natoque penatibus et magnis dis parturient montes,</p>
      </div>
    </article>
    <article class="listing" style="top:423px">
      <div class="photo" role="img" aria-label="Photo of a suburban house with double garage" style="background:linear-gradient(#5a92d6,#c6c2b2 55%,#5a8a34)"></div>
      <div class="info">
        <h4>Tala 2 bedroom Apartments</h4>
        <div class="meta"><span>Area : 117 (Sq.M.)</span><span>Property ID : 14353</span><span>Bedrooms : 3</span><span>Posted on : March 2, 2013</span></div>
        <p>Mauris vel lacus vitae felis vestibulum volutpat. Etiam est nunc, venenatis in, tristique eu, imperdiet ac, nisl. Cum sociis natoque penatibus et magnis dis parturient montes,</p>
      </div>
    </article>
  </section>

  <aside class="abs news">
    <h2>Latest News</h2>
    <div class="entry"><time>20 Feb 2013</time><p>Etiam est nunc, venenatis in, tristique eu, imperdiet ac, nisl. Cum sociis natoque penatibus et magnis dis parturient montes,</p></div>
    <div class="entry"><time>10 Feb 2013</time><p>Etiam est nunc, venenatis in, tristique eu, imperdiet ac, nisl. Cum sociis natoque</p></div>
    <div class="entry"><time>03 Feb 2013</time><p>Etiam est nunc, venenatis in, tristique eu, imperdiet ac, nisl. Cum sociis natoque</p></div>
    <div class="entry"><time>05 Feb 2013</time><p>Etiam est nunc, venenatis in, tristique eu, imperdiet ac, nisl. Cum sociis natoque</p></div>
  </aside>

  <aside class="abs top">
    <h2>Top Property</h2>
    <ul>
      <li>Mauris vel lacus vitae</li>
      <li>Felis vestibulum volutpat.</li>
      <li>Etiam est nunc venenatis</li>
      <li>Tristique eu imperdiet</li>
      <li>Cum sociis natoque</li>
      <li>Penatibus et magnis</li>
    </ul>
  </aside>

  <footer class="abs footer">
    <div class="copy">Copyright © 2012 Company Name. All right reserved. &nbsp;Term of Use</div>
    <div class="flinks">Home<span>|</span>Our Listings<span>|</span>Buyers<span>|</span>Short Sales<span>|</span>Agents<span>|</span>Asset Managers<span>|</span>Contact Us</div>
    <div class="social"><i></i><i></i><i></i></div>
  </footer>
</div>
</body>
</html>
```